INNOVATIVE DESIGN NEEDED FOR FINANCIAL COMPANY

INTERNATIONAL FIRM IN HONG KONG NEEDS A MODERN BUSINESS CARD DESIGN. ONE SIDE ENGLISH OTHER SIDE IN CHINESE. WE ARE OPEN TO CHANGING FONTS AND COLOR. SHOULD BE A CARD THAT IS PROFESSIONAL DEALING WITH HIGH NET WORTH CLIENTELE. BOTH SIDES OF THE CARD WILL BE THE SAME, HOWEVER, THE WORDING ON ONE SIDE WILL BE ENGLISH AND THE OTHER SIDE IN CHINESE (CAN ASSIST IN THE LETTERING - CAN PROVIDE ONCE CARD DESIGN IS ACCEPTED.

Target Market(s)

Hong Kong/CHINA

Contact Information for Business Card

ATTRACTIVE MODERN

```html
<!DOCTYPE html>
<html lang="en">
<head>
<meta charset="utf-8">
<title>Larchfield Capital Partners – Business Card</title>
<link rel="stylesheet" href="https://fonts.googleapis.com/css2?family=Montserrat:wght@400;500;700&family=Noto+Sans+TC:wght@400;500;900&display=swap">
<style>
  :root {
    --backdrop: #d9d9d6;
    --paper: #f1f1ee;
    --charcoal: #1f2220;
    --ink: #3a3c3b;
    --green: #0e8c5c;
    --muted: #c9ccca;
  }
  * { box-sizing: border-box; margin: 0; padding: 0; }
  html, body { width: 1200px; height: 901px; overflow: hidden; }
  body {
    background: var(--backdrop);
    font-family: "Montserrat", "Noto Sans TC", sans-serif;
    display: flex;
    align-items: center;
    justify-content: center;
    gap: 50px;
  }
  .card {
    position: relative;
    width: 540px;
    height: 309px;
    background: var(--charcoal);
    box-shadow: 0 10px 30px rgba(0,0,0,.25);
    overflow: hidden;
  }
  .card__head {
    height: 145px;
    background: var(--paper);
    border-bottom: 4px solid var(--green);
    display: flex;
    align-items: center;
    padding-left: 42px;
    gap: 18px;
  }
  .brand__dot {
    width: 54px; height: 54px;
    border-radius: 50%;
    background: var(--green);
    flex: none;
  }
  .brand__text { color: var(--ink); font-weight: 900; font-family: "Noto Sans TC", sans-serif; line-height: 1.15; }
  .brand__zh { font-size: 27px; letter-spacing: 2px; }
  .brand__en { font-size: 11.5px; letter-spacing: 1.4px; }
  .person {
    position: absolute;
    left: 42px; top: 182px;
    color: #fff;
  }
  .person__name { color: var(--green); font-size: 25px; font-weight: 500; }
  .person__title { font-size: 16px; font-weight: 400; margin-top: 2px; }
  .person__address { font-size: 11px; color: var(--muted); margin-top: 16px; line-height: 1.45; }
  .card--zh .person__name, .card--zh .person__title, .card--zh .person__address { font-family: "Noto Sans TC", sans-serif; }
  .contact {
    position: absolute;
    right: 34px; top: 168px;
    list-style: none;
    color: #fff;
    font-size: 12px;
    line-height: 1;
  }
  .contact li { display: flex; align-items: center; gap: 10px; margin-bottom: 8px; }
  .contact svg { width: 12px; height: 12px; flex: none; }
</style>
</head>
<body>

  <article class="card card--en">
    <header class="card__head">
      <span class="brand__dot"></span>
      <div class="brand__text">
        <div class="brand__zh">樺峰資本管理有限公司</div>
        <div class="brand__en">Larchfield Capital Partners Ltd</div>
      </div>
    </header>
    <div class="person">
      <div class="person__name">Alex Chan</div>
      <div class="person__title">Manager</div>
      <div class="person__address">18 Harbour View Tower<br>Canal Rd, HONG KONG</div>
    </div>
    <ul class="contact">
      <li><svg viewBox="0 0 12 12"><path d="M3 1 L5 3.5 L4 5 Q5.5 7.5 7 8 L8.5 7 L11 9 L9.5 11 Q3.5 10 1 2.5 Z" fill="#0e8c5c"/></svg>555-210-4830</li>
      <li><svg viewBox="0 0 12 12"><rect x="1" y="2.5" width="10" height="7" fill="#0e8c5c"/><path d="M1 2.5 L6 6.5 L11 2.5" stroke="#1f2220" fill="none"/></svg>alex.chan@larchfield.com</li>
      <li><svg viewBox="0 0 12 12"><circle cx="6" cy="6" r="5" fill="none" stroke="#0e8c5c" stroke-width="1.3"/><ellipse cx="6" cy="6" rx="2.2" ry="5" fill="none" stroke="#0e8c5c"/><path d="M1 6 H11" stroke="#0e8c5c"/></svg>www.larchfield.com</li>
    </ul>
  </article>

  <article class="card card--zh" lang="zh-Hant">
    <header class="card__head">
      <span class="brand__dot"></span>
      <div class="brand__text">
        <div class="brand__zh">樺峰資本管理有限公司</div>
        <div class="brand__en">Larchfield Capital Partners Ltd</div>
      </div>
    </header>
    <div class="person">
      <div class="person__name">陳志明</div>
      <div class="person__title">經理</div>
      <div class="person__address">香港運河道<br>海景大廈18號</div>
    </div>
    <ul class="contact">
      <li><svg viewBox="0 0 12 12"><path d="M3 1 L5 3.5 L4 5 Q5.5 7.5 7 8 L8.5 7 L11 9 L9.5 11 Q3.5 10 1 2.5 Z" fill="#0e8c5c"/></svg>555-210-4830</li>
      <li><svg viewBox="0 0 12 12"><rect x="1" y="2.5" width="10" height="7" fill="#0e8c5c"/><path d="M1 2.5 L6 6.5 L11 2.5" stroke="#1f2220" fill="none"/></svg>alex.chan@larchfield.com</li>
      <li><svg viewBox="0 0 12 12"><circle cx="6" cy="6" r="5" fill="none" stroke="#0e8c5c" stroke-width="1.3"/><ellipse cx="6" cy="6" rx="2.2" ry="5" fill="none" stroke="#0e8c5c"/><path d="M1 6 H11" stroke="#0e8c5c"/></svg>www.larchfield.com</li>
    </ul>
  </article>

</body>
</html>
```